Tidal Oak Business Cards

We need something new, fun and exciting for business cards. Our current ones are just plain and we need a design that pops. We want name, position held, phone, email on the front, and a 20% discount on the back. I have also uploaded our old business cards creative to see what we are not wanting, and how boring they were and we want something jazzed up from this, cool design and catches people attention.

```html
<!DOCTYPE html>
<html lang="en">
<head>
<meta charset="utf-8">
<title>Tidal Oak Business Cards</title>
<link rel="stylesheet" href="https://fonts.googleapis.com/css2?family=Open+Sans:wght@300;400;600;700;800&display=swap">
<style>
  :root {
    --bg: #8a8580;
    --coral: #ef6461;
    --navy: #1c3a6e;
    --ink: #4a4a4a;
    --paper: #ffffff;
    --night: #181818;
    --night-soft: #303030;
  }
  * { box-sizing: border-box; margin: 0; padding: 0; }
  html, body { width: 1200px; height: 900px; overflow: hidden; }
  body {
    background: var(--bg);
    font-family: "Open Sans", Arial, sans-serif;
    position: relative;
  }
  .card {
    position: absolute;
    left: 300px;
    width: 600px;
    height: 380px;
    border-radius: 38px;
    overflow: hidden;
    box-shadow: 0 14px 30px rgba(0,0,0,0.35);
  }
  .card-front {
    top: 40px;
    background: var(--paper);
    border: 8px solid var(--coral);
  }
  .card-back {
    top: 470px;
    background: var(--night);
  }
  .brand {
    position: absolute;
    left: 40px;
    top: 58px;
    display: flex;
    align-items: center;
    gap: 14px;
  }
  .brand-dot {
    width: 30px; height: 30px;
    border-radius: 50%;
    background: var(--coral);
  }
  .brand-name {
    font-size: 54px;
    font-weight: 600;
    color: var(--navy);
    letter-spacing: -1px;
    line-height: 1;
  }
  .person {
    position: absolute;
    left: 300px;
    top: 150px;
    width: 250px;
  }
  .person-name {
    font-size: 24px;
    color: var(--ink);
    line-height: 1.1;
  }
  .person-name strong { font-weight: 700; }
  .person-name span { font-weight: 300; }
  .person-role {
    font-size: 14px;
    color: var(--ink);
    text-align: right;
    padding-right: 40px;
    margin-top: 2px;
  }
  .rule {
    height: 2px;
    background: var(--navy);
    margin: 6px 0 10px;
    width: 220px;
  }
  .contacts { list-style: none; }
  .contact {
    display: flex;
    align-items: center;
    gap: 12px;
    margin-bottom: 7px;
    font-size: 12.5px;
    color: var(--ink);
    line-height: 1.3;
  }
  .contact:last-child { margin-bottom: 0; }
  .contact-icon {
    flex: 0 0 26px;
    width: 26px; height: 26px;
    border-radius: 50%;
    background: var(--navy);
    display: flex;
    align-items: center;
    justify-content: center;
  }
  .contact-icon svg { width: 14px; height: 14px; fill: #fff; }
  .pattern {
    position: absolute;
    inset: 0;
    background:
      radial-gradient(ellipse at 30% 30%, rgba(80,80,80,0.35), transparent 55%),
      radial-gradient(ellipse at 75% 75%, rgba(70,70,70,0.3), transparent 55%),
      linear-gradient(135deg, var(--night-soft), var(--night));
  }
  .offer {
    position: absolute;
    inset: 0;
    display: flex;
    flex-direction: column;
    align-items: center;
    justify-content: center;
    color: var(--coral);
    font-weight: 800;
    line-height: 0.95;
  }
  .offer-amount { font-size: 84px; letter-spacing: 4px; }
  .offer-label { font-size: 60px; letter-spacing: 8px; }
</style>
</head>
<body>
  <section class="card card-front">
    <div class="brand">
      <div class="brand-dot"></div>
      <div class="brand-name">Tidal Oak</div>
    </div>
    <div class="person">
      <p class="person-name"><strong>Lorem</strong> <span>ipsum</span></p>
      <p class="person-role">Designer</p>
      <div class="rule"></div>
      <ul class="contacts">
        <li class="contact">
          <span class="contact-icon"><svg viewBox="0 0 16 16"><path d="M8 1 1 7.5h2V15h4v-4h2v4h4V7.5h2z"/></svg></span>
          <span>Street Address Here<br>Italy, 2222</span>
        </li>
        <li class="contact">
          <span class="contact-icon"><svg viewBox="0 0 16 16"><path d="M15 1 1 7l5 2 2 5z"/></svg></span>
          <span>username@email.com</span>
        </li>
        <li class="contact">
          <span class="contact-icon"><svg viewBox="0 0 16 16"><path d="M4 1 6.5 4 5 6c1 2 3 4 5 5l2-1.5 3 2.5-2 2.5C7 14 2 9 1.5 3z"/></svg></span>
          <span>+77 7777 7777 7777<br>+55 6767 4545 2323</span>
        </li>
      </ul>
    </div>
  </section>

  <section class="card card-back">
    <div class="pattern" role="img" aria-label="Repeating embossed leaf and heart pattern in dark grey"></div>
    <div class="offer">
      <span class="offer-amount">20%</span>
      <span class="offer-label">OFF</span>
    </div>
  </section>
</body>
</html>
```